HTML formatted email for Brightvarna

Create a single email in html format to describe the Brightvarna product.

It needs to be based on the brochure design (supplied) and using existing logo.
One requirement is that the background of the email has to be a set color (grey), regardless of how large the viewer opens the email window.
It will be a mix of graphics and text: and the central block of content within the email must remain intact and true regardless of how the viewer resizes the email window.
The html email must be viewable in it true format on all common email programs, including Microsoft Outlook, horde, gmail and others.

The attached file is for reference only, full PSD will be supplied to winner. (The actual text content will be different to the sample file)

```html
<!DOCTYPE html>
<html lang="en">
<head>
<meta charset="utf-8">
<title>Brightvarna – Your data, when you need it</title>
<link rel="stylesheet" href="https://fonts.googleapis.com/css2?family=Arimo:wght@400;700&display=swap">
<style>
  :root {
    --page-bg: #2a2a2e;
    --card-bg: #ffffff;
    --sky: #7fcff5;
    --brand-blue: #229fe0;
    --ink: #2a2a2e;
    --body-text: #444448;
    --muted: #b9b9bd;
  }
  * { box-sizing: border-box; margin: 0; padding: 0; }
  html, body {
    width: 1200px; height: 1200px; overflow: hidden;
    background: var(--page-bg);
    font-family: "Arimo", Arial, sans-serif;
  }
  .mailer { position: relative; width: 1200px; height: 1200px; }

  .view-online {
    position: absolute; top: 24px; right: 305px;
    font-size: 11px; color: var(--muted);
  }
  .view-online a { color: var(--muted); margin-left: 4px; }

  .header-card {
    position: absolute; left: 300px; top: 43px; width: 600px; height: 252px;
    background: var(--card-bg);
    border-top: 8px solid var(--sky);
    border-radius: 8px;
    overflow: hidden;
  }
  .brand-dot {
    position: absolute; left: 50%; top: 26px; transform: translateX(-50%);
    width: 100px; height: 100px; border-radius: 50%; background: var(--sky);
  }
  .brand-name {
    position: absolute; left: 0; right: 0; top: 138px;
    text-align: center; font-size: 50px; font-weight: 400;
    color: var(--ink); letter-spacing: -1px;
  }
  .tagline-band {
    position: absolute; left: 0; right: 0; bottom: 0; height: 43px;
    background: var(--brand-blue);
    color: #fff; font-weight: 700; font-size: 22px;
    text-align: center; line-height: 43px;
  }

  .content-card {
    position: absolute; left: 301px; top: 303px; width: 600px; height: 684px;
    background: var(--card-bg);
    border-top: 7px solid var(--sky);
    border-radius: 8px;
  }
  .pointer { position: absolute; left: 574px; top: 295px; }

  .intro {
    position: absolute; left: 50px; right: 50px; top: 32px;
    text-align: center; font-size: 14px; line-height: 17px; color: var(--body-text);
  }
  .intro-strap {
    position: absolute; left: 0; right: 0; top: 100px;
    text-align: center; font-size: 13px; font-weight: 700; color: var(--body-text);
  }
  .cta {
    position: absolute; left: 204px; top: 131px; width: 208px; height: 51px;
    background: var(--sky); border-radius: 6px;
    color: #fff; font-size: 22px; font-weight: 700;
    text-align: center; line-height: 51px; text-decoration: none;
  }
  .divider {
    position: absolute; left: 49px; width: 500px; top: 195px;
    border-top: 1px dotted #666;
  }

  .feature { position: absolute; left: 45px; width: 510px; }
  .feature-title {
    position: relative; padding-left: 25px;
    font-size: 20px; font-weight: 400; color: var(--brand-blue); line-height: 24px;
  }
  .feature-title::before {
    content: ""; position: absolute; left: 2px; top: 7px;
    width: 11px; height: 11px; border-radius: 50%;
    background: var(--sky); border: 2px solid var(--ink);
  }
  .feature-text {
    padding-left: 26px; margin-top: 4px;
    font-size: 12px; line-height: 14px; color: var(--body-text);
  }

  .footer {
    position: absolute; top: 999px; left: 0; right: 0;
    text-align: center; font-size: 11px; color: var(--muted);
  }
  .footer a { color: var(--muted); }
  .footer .sep { margin: 0 14px; }
</style>
</head>
<body>
<div class="mailer">
  <p class="view-online">View this mailer online. <a href="#">Click here</a></p>

  <header class="header-card">
    <div class="brand-dot"></div>
    <div class="brand-name">Brightvarna</div>
    <h1 class="tagline-band">Your data - when you need it, where you need it</h1>
  </header>

  <main class="content-card">
    <p class="intro">Brightvarna is everything you would expect from a cloud storage provider with one major advantage - your data is stored locally which means you can access your information with <em>or</em> without internet access.</p>
    <p class="intro-strap">It's secure, cost effective and easy!</p>
    <a class="cta" href="#">Learn more</a>
    <div class="divider"></div>

    <section class="feature" style="top:219px">
      <h2 class="feature-title">Automated file backups to the cloud</h2>
      <p class="feature-text">Lorem ipsum dolor sit amet, consectetur adipiscing elit. Duis in eros vitae purus vulputate dictum quis egestas magna. Vivamus interdum nisl eget cursus tempor.</p>
    </section>
    <section class="feature" style="top:298px">
      <h2 class="feature-title">Stashbox-style data storage service</h2>
      <p class="feature-text">Lorem ipsum dolor sit amet, consectetur adipiscing elit. Duis in eros vitae purus vulputate dictum quis egestas magna. Vivamus interdum nisl eget cursus tempor. Donec ut ligula fermentum, imperdiet diam a, porttitor sapien. Proin auctor leo felis, eget ...</p>
    </section>
    <section class="feature" style="top:384px">
      <h2 class="feature-title">Desktop file synchronisation</h2>
      <p class="feature-text" style="margin-top:0">Lorem ipsum dolor sit amet, consectetur adipiscing elit. Duis in eros vitae purus vulputate dictum quis egestas magna. Vivamus interdum nisl eget cursus tempor.</p>
    </section>
    <section class="feature" style="top:456px">
      <h2 class="feature-title">Version control of stored files</h2>
      <p class="feature-text" style="margin-top:0">Lorem ipsum dolor sit amet, consectetur adipiscing elit. Duis in eros vitae purus vulputate dictum quis egestas magna. Vivamus interdum nisl eget cursus tempor.</p>
    </section>
    <section class="feature" style="top:525px">
      <h2 class="feature-title">Cloud-based Contacts, Address Books &amp; Calendar</h2>
      <p class="feature-text" style="margin-top:0">Lorem ipsum dolor sit amet, consectetur adipiscing elit. Duis in eros vitae purus vulputate dictum quis egestas magna. Vivamus interdum nisl eget cursus tempor.</p>
    </section>
    <section class="feature" style="top:595px">
      <h2 class="feature-title">Mobile device compatible</h2>
      <p class="feature-text" style="margin-top:0">Lorem ipsum dolor sit amet, consectetur adipiscing elit. Duis in eros vitae purus vulputate dictum quis egestas magna. Vivamus interdum nisl eget cursus tempor.</p>
    </section>
  </main>

  <svg class="pointer" width="52" height="34" viewBox="0 0 52 34" aria-hidden="true">
    <polygon points="4,8 48,8 26,33" fill="var(--sky)"/>
    <polygon points="2,0 50,0 26,24" fill="var(--brand-blue)"/>
  </svg>

  <footer class="footer">
    Copyright © 2014 Brightvarna<span class="sep">|</span><a href="#">Disclaimer</a><span class="sep">|</span><a href="#">Privacy Policy</a><span class="sep" style="margin:0 10px">|</span><a href="#">Unsubscribe</a>
  </footer>
</div>
</body>
</html>
```